THE WELLNESS BARN WEBSITE for Physio, Fitness, health

An attractive website advertising a physiotherapyand fitness / gym business, not generic, colours are natural, greens, browns, beiges. No cheesy pictures. With the ability to sell a small,amount of goods online if i decide to. Simple to navigate. Text boxes that i can input the main information and change easily. Somewhere to put my timetable. Easy to find contact details. However many pages it needs, im not fussed.
Target Market(s)
People looking for rehabilitation or fitness classes
Industry/Entity Type
Physiotherapy, Fitness, Gym, Health
Coding
Coded - Design and coding required
Number of Pages Required
1 page
Font styles to use
Other font styles liked:
- Im not fusse,ld, not script
Requirements
Must have
- Will upload posts from my business insta page for reference about the feel. Earthy natural tones, I have a lot of timber, and rustic looking piece's, plants etc in my clinic
Nice to have
- Simple to navigate
Should not have
- Cheesy "yoga" or generic "people doing physio" pics

```html
<!DOCTYPE html>
<html lang="en">
<head>
<meta charset="utf-8">
<title>The Wellness Barn — Physiotherapy &amp; Fitness</title>
<link href="https://fonts.googleapis.com/css2?family=Lato:wght@400;700;900&display=swap" rel="stylesheet">
<style>
:root{
  --green:#5b7f1f;
  --green-mid:#4f7018;
  --green-dark:#2f4316;
  --ink:#262b22;
  --text:#4a4f45;
  --pale:#f2f6e2;
  --pale-line:#dfe8c2;
  --footer:#10140b;
  --footer-bar:#3b4b1c;
  --star:#f2b418;
  --white:#ffffff;
}
*{box-sizing:border-box;margin:0;padding:0}
html,body{width:1200px;height:5063px;overflow:hidden}
body{font-family:'Lato',sans-serif;color:var(--text);background:var(--white);position:relative}
section,header,footer{position:relative;width:1200px}
.abs{position:absolute}
.photo{position:absolute;display:block}
.btn{position:absolute;display:flex;align-items:center;justify-content:center;background:var(--green);color:var(--white);font-weight:700;font-size:14px;border-radius:22px}
.btn.dark{background:var(--green-dark)}
.h2{font-weight:700;color:var(--ink);font-size:40px;letter-spacing:-0.5px;text-transform:uppercase}
.arrow{position:absolute;width:38px;height:38px;border-radius:50%;background:var(--green-dark);display:flex;align-items:center;justify-content:center}

/* header */
.site-header{height:171px}
.topbar{position:absolute;left:412px;top:0;width:788px;height:55px;background:var(--green-dark);clip-path:polygon(0 0,100% 0,100% 100%,34px 100%)}
.topbar .contact{position:absolute;top:10px;display:flex;align-items:center;gap:14px;color:var(--white);font-size:14px}
.topbar .ico{width:36px;height:36px;border-radius:50%;background:var(--green);display:flex;align-items:center;justify-content:center}
.brand{position:absolute;left:112px;top:34px;display:flex;align-items:center;gap:12px}
.brand .mark{width:28px;height:28px;border-radius:50%;background:var(--green-dark)}
.brand .name{font-weight:900;font-size:34px;line-height:36px;color:var(--green-dark);text-transform:uppercase}
.nav{position:absolute;top:104px;left:444px;display:flex;gap:38px;font-size:15px;color:var(--text)}
.nav .active{color:var(--green);font-weight:700;border-bottom:2px solid var(--green);padding-bottom:2px}

/* hero */
.hero{height:599px}
.hero .panel{position:absolute;left:0;top:0;width:601px;height:599px;background:rgba(86,126,25,.93);border-radius:0 0 22px 0}
.hero h1{position:absolute;left:112px;top:138px;color:var(--white);font-size:54px;line-height:64px;font-weight:700;text-transform:uppercase;letter-spacing:-0.5px}
.hero p{position:absolute;left:112px;top:352px;width:400px;color:var(--white);font-size:17px;line-height:26px}

/* about */
.about{height:760px}
.about .h2{position:absolute;left:701px;top:80px}
.about .intro{position:absolute;left:701px;top:144px;width:390px;font-size:14px;line-height:24px}
.value{position:absolute;left:701px;width:400px;height:80px}
.value .badge{position:absolute;left:0;top:4px;width:62px;height:62px;border-radius:50%;background:var(--green);display:flex;align-items:center;justify-content:center}
.value h3{position:absolute;left:90px;top:0;font-size:17px;font-weight:700;color:var(--ink)}
.value p{position:absolute;left:92px;top:30px;width:300px;font-size:12.5px;line-height:22px;height:44px;overflow:hidden}

/* offers */
.offers{height:627px}
.offers .h2{position:absolute;left:0;width:1200px;text-align:center;top:68px}
.offer{position:absolute;top:127px;width:298px}
.offer .img{height:316px;border-radius:6px}
.offer h3{margin-top:20px;text-align:center;font-size:22px;line-height:27px;font-weight:700;color:var(--green)}

/* program */
.program{height:508px}
.program .copy{position:absolute;left:212px;top:0;width:599px;height:508px;background:var(--green)}
.program h2{position:absolute;left:96px;top:60px;color:var(--white);font-size:38px;line-height:48px;font-weight:700;text-transform:uppercase}
.program .lead{position:absolute;left:96px;top:174px;width:460px;color:var(--white);font-size:13.5px;line-height:24px}
.stat{position:absolute;left:96px;color:var(--white)}
.stat .ico{position:absolute;left:0;top:0}
.stat b{position:absolute;left:82px;top:2px;font-size:18px;font-weight:700;white-space:nowrap}
.stat span{position:absolute;left:82px;top:36px;font-size:13.5px;white-space:nowrap}

/* products */
.products{height:758px}
.products .h2{position:absolute;left:0;width:1200px;text-align:center;top:60px}
.product{position:absolute;top:118px;width:295px;text-align:center}
.product .img{height:322px;border-radius:4px}
.product h3{margin-top:20px;font-size:21px;font-weight:700;color:var(--ink)}
.product p{margin:10px auto 0;width:240px;font-size:13.5px;line-height:18px}
.product .price{margin-top:18px;font-size:23px;font-weight:700;color:var(--green)}
.product .btn{position:relative;margin:14px auto 0;width:156px;height:41px;font-size:14px}
.dots{position:absolute;top:3195px;}

/* faqs */
.faqs{height:601px}
.faqs .h2{position:absolute;left:112px;top:12px;font-size:42px}
.faqs .intro{position:absolute;left:112px;top:82px;width:390px;font-size:14px;line-height:24px}
.faq{position:absolute;left:112px;width:399px;height:40px;border-radius:20px;background:var(--pale);border:1px solid var(--pale-line);display:flex;align-items:center;justify-content:space-between;padding:0 24px 0 26px;font-size:14px;font-weight:700;color:var(--ink)}
.faq.open{background:var(--green);color:var(--white);border-color:var(--green)}
.faqs .answer{position:absolute;left:112px;top:202px;width:390px;font-size:13.5px;line-height:24px}

/* stories */
.stories{height:544px}
.stories .h2{position:absolute;left:0;width:1200px;text-align:center;top:0}
.stories .sub{position:absolute;left:0;width:1200px;text-align:center;top:50px;color:var(--green);font-size:18px}
.story{position:absolute;top:94px;width:308px;height:362px;background:var(--white);box-shadow:0 2px 14px rgba(0,0,0,.09);border-bottom:6px solid var(--green);text-align:center}
.story .avatar{width:90px;height:90px;border-radius:50%;margin:39px auto 0;background:radial-gradient(circle at 50% 40%,#d9b49a,#8a5c3f)}
.story h3{margin-top:22px;font-size:22px;font-weight:700;color:var(--ink)}
.story p{margin:12px auto 0;width:260px;font-size:13px;line-height:22px}
.story .role{margin-top:12px;font-size:14px;font-weight:700;color:var(--green)}
.story .stars{margin-top:8px;color:var(--star);font-size:18px;letter-spacing:2px}

/* footer */
.site-footer{height:632px;background:var(--footer);color:var(--white)}
.site-footer h4{position:absolute;font-size:22px;font-weight:700}
.site-footer .small{position:absolute;font-size:14px;line-height:25px}
.email-field{position:absolute;left:526px;top:80px;width:403px;height:44px;border:1px solid #7f8a6a;border-radius:22px;display:flex;align-items:center;justify-content:space-between;padding:0 24px;font-size:12.5px}
.fcol{position:absolute;top:274px}
.fcol h4{position:static;margin-bottom:22px}
.fcol ul{list-style:none;font-size:14px}
.fcol li{height:39px}
.social{position:absolute;top:432px;left:112px;display:flex;gap:12px}
.social i{display:block;width:36px;height:36px;border-radius:6px;background:var(--green)}
.social i+i{background:transparent;border:2px solid var(--white);border-radius:8px;width:26px;height:26px;margin-top:5px}
.copyright{position:absolute;left:0;top:569px;width:1200px;height:63px;background:var(--footer-bar);display:flex;align-items:center;justify-content:center;font-size:13px}
</style>
</head>
<body>

<header class="site-header">
  <div class="topbar">
    <div class="contact" style="left:194px">
      <span class="ico"><svg width="16" height="16" viewBox="0 0 24 24" fill="none" stroke="#fff" stroke-width="2"><path d="M5 3h4l2 5-2.5 1.5a11 11 0 0 0 6 6L16 13l5 2v4a2 2 0 0 1-2 2A17 17 0 0 1 3 5a2 2 0 0 1 2-2"/></svg></span>+61 400 555 218
    </div>
    <div class="contact" style="left:422px">
      <span class="ico"><svg width="16" height="16" viewBox="0 0 24 24" fill="none" stroke="#fff" stroke-width="2"><rect x="3" y="5" width="18" height="14" rx="2"/><path d="M3 7l9 6 9-6"/></svg></span>hello@wellnessbarnhq.com
    </div>
  </div>
  <div class="brand"><span class="mark"></span><span class="name">The Wellness<br>Barn</span></div>
  <nav class="nav">
    <span class="active">Home</span><span>About Us</span><span>Programs</span><span>Testimonials</span><span>Contact</span>
  </nav>
  <span class="btn" style="left:933px;top:92px;width:155px;height:42px">Join the Barn</span>
</header>

<section class="hero">
  <div class="photo" role="img" aria-label="Photo of four clinic members in team singlets standing arm in arm outdoors" style="left:0;top:0;width:1200px;height:599px;background:linear-gradient(180deg,#6d9ac3 0%,#a9c2d2 28%,#5f6c3c 55%,#2c2d25 80%,#8a7a5d 100%)"></div>
  <div class="panel"></div>
  <h1>Move better.<br>Feel stronger.<br>Live well.</h1>
  <p>Discover holistic physiotherapy and fitness in a space inspired by nature and wellness.</p>
  <span class="btn dark" style="left:112px;top:438px;width:144px;height:40px">Get Started</span>
</section>

<section class="about">
  <div class="photo" role="img" aria-label="Photo of the clinic group standing together inside the gym" style="left:112px;top:86px;width:497px;height:499px;border-radius:8px;background:linear-gradient(180deg,#6e6e68 0%,#4a4943 45%,#2a2b27 70%,#7a7870 100%)"></div>
  <h2 class="h2">About Us</h2>
  <p class="intro">At The Wellness Barn Riverbend, we are dedicated to empowering individuals through safe and effective movement. Our mission is to enhance your health and wellbeing with professional support.</p>
  <div class="value" style="top:266px">
    <span class="badge"><svg width="32" height="32" viewBox="0 0 24 24" fill="none" stroke="#fff" stroke-width="1.6"><circle cx="12" cy="12" r="9"/><circle cx="12" cy="12" r="5"/><circle cx="12" cy="12" r="1.5"/></svg></span>
    <h3>Our Mission</h3><p>We aim to empower individuals to achieve their health and wellness goals through safe and personalised care.</p>
  </div>
  <div class="value" style="top:354px">
    <span class="badge"><svg width="32" height="32" viewBox="0 0 24 24" fill="none" stroke="#fff" stroke-width="1.6"><path d="M12 21s-7-4.5-7-10a4 4 0 0 1 7-2.5A4 4 0 0 1 19 11c0 5.5-7 10-7 10z"/></svg></span>
    <h3>Our Values</h3><p>We uphold values of integrity, collaboration, and inclusivity. Our commitment to health and community guides us.</p>
  </div>
  <div class="value" style="top:438px">
    <span class="badge"><svg width="32" height="32" viewBox="0 0 24 24" fill="none" stroke="#fff" stroke-width="1.6"><circle cx="8" cy="8" r="3"/><circle cx="16" cy="8" r="3"/><path d="M3 19c0-3 2.5-5 5-5s5 2 5 5M11 19c0-3 2.5-5 5-5s5 2 5 5"/></svg></span>
    <h3>Meet Our Team</h3><p>Our team includes experienced professionals like Dr. Clara Whitfield, our Lead Physiotherapist, and more.</p>
  </div>
  <span class="btn" style="left:701px;top:530px;width:156px;height:40px">Read More</span>
</section>

<section class="offers">
  <h2 class="h2">What do we have to offer?</h2>
  <span class="arrow" style="left:50px;top:327px"><svg width="14" height="14" viewBox="0 0 24 24" fill="none" stroke="#fff" stroke-width="3"><path d="M15 5l-7 7 7 7"/></svg></span>
  <div class="offer" style="left:112px">
    <div class="img" role="img" aria-label="Photo of a physiotherapy group class with exercise balls" style="background:linear-gradient(180deg,#d9dcd8,#a9b3ad 55%,#8a8f90)"></div>
    <h3>Physiotherapy Classes<br>for Everyone</h3>
  </div>
  <div class="offer" style="left:452px">
    <div class="img" role="img" aria-label="Photo of a wellness planning session at a table" style="background:linear-gradient(180deg,#3a2a1e,#7a5030 55%,#2e2218)"></div>
    <h3>Holistic Wellness<br>Programs</h3>
  </div>
  <div class="offer" style="left:790px">
    <div class="img" role="img" aria-label="Photo of a calm mindfulness session in a bright room" style="background:linear-gradient(180deg,#e9e6dd,#cbc6b8 55%,#9d9889)"></div>
    <h3>Mindfulness and Yoga<br>Sessions</h3>
  </div>
  <span class="arrow" style="left:1110px;top:327px"><svg width="14" height="14" viewBox="0 0 24 24" fill="none" stroke="#fff" stroke-width="3"><path d="M9 5l7 7-7 7"/></svg></span>
</section>

<section class="program">
  <div class="photo" role="img" aria-label="Photo of a festive group workout in the gym" style="left:0;top:0;width:206px;height:508px;background:linear-gradient(180deg,#77756c,#504e47 55%,#6a665c)"></div>
  <div class="copy">
    <h2>Discover our unique<br>health program</h2>
    <p class="lead">Our featured program offers a comprehensive approach to health, focusing on safe movement and personalized support. Led by experienced physiotherapists, it is designed to enhance your wellbeing and help you achieve your health goals effectively.</p>
    <div class="stat" style="top:292px">
      <svg class="ico" width="50" height="50" viewBox="0 0 24 24" fill="none" stroke="#fff" stroke-width="1.2"><rect x="3" y="5" width="16" height="15" rx="2"/><path d="M3 9h16M7 3v4M15 3v4"/><circle cx="18" cy="18" r="4" fill="#5b7f1f"/><path d="M16.5 18l1 1 2-2"/></svg>
      <b>12 weeks</b><span>Program duration to ensure lasting results.</span>
    </div>
    <div class="stat" style="top:380px">
      <svg class="ico" width="54" height="50" viewBox="0 0 26 24" fill="none" stroke="#fff" stroke-width="1.2"><circle cx="13" cy="12" r="10"/><rect x="3" y="9" width="20" height="6" rx="1" fill="#5b7f1f"/><text x="13" y="14" font-size="5" fill="#fff" stroke="none" text-anchor="middle" font-family="Lato, sans-serif">100%</text></svg>
      <b>100 %</b><span>Client satisfaction rate with our program.</span>
    </div>
  </div>
  <div class="photo" role="img" aria-label="Photo of three team members smiling outside the clinic at dusk" style="left:817px;top:0;width:383px;height:508px;background:linear-gradient(180deg,#3e4a55,#2b2a28 50%,#5b4c3e)"></div>
  <span class="arrow" style="left:188px;top:235px"><svg width="14" height="14" viewBox="0 0 24 24" fill="none" stroke="#fff" stroke-width="3"><path d="M15 5l-7 7 7 7"/></svg></span>
  <span class="arrow" style="left:795px;top:235px"><svg width="14" height="14" viewBox="0 0 24 24" fill="none" stroke="#fff" stroke-width="3"><path d="M9 5l7 7-7 7"/></svg></span>
</section>

<section class="products">
  <h2 class="h2">Our Products</h2>
  <div class="product" style="left:112px">
    <div class="img" role="img" aria-label="Photo of a branded drink cooler among dried flowers" style="background:linear-gradient(180deg,#b59b7c,#6e4a3c 50%,#b7ad8e)"></div>
    <h3>Lorem Ipsum</h3><p>Risus commodo viverra maecenas accumsan lacus vel facilisis.</p><div class="price">$50.00</div><span class="btn">Shop Now</span>
  </div>
  <div class="product" style="left:452px">
    <div class="img" role="img" aria-label="Photo of a branded green cap on a grey shirt" style="background:linear-gradient(180deg,#c6a792,#8d8c86 45%,#b4b3ad)"></div>
    <h3>Lorem Ipsum</h3><p>Risus commodo viverra maecenas accumsan lacus vel facilisis.</p><div class="price">$50.00</div><span class="btn">Shop Now</span>
  </div>
  <div class="product" style="left:793px">
    <div class="img" role="img" aria-label="Photo of an amber spray bottle among plants" style="background:linear-gradient(180deg,#4f6a38,#2e4528 50%,#6b7d4c)"></div>
    <h3>Lorem Ipsum</h3><p>Risus commodo viverra maecenas accumsan lacus vel facilisis.</p><div class="price">$50.00</div><span class="btn">Shop Now</span>
  </div>
  <svg class="abs" style="left:563px;top:551px" width="74" height="6"><rect width="18" height="5" rx="2.5" fill="#2f4316"/><rect x="28" width="18" height="5" rx="2.5" fill="#cfd3c8"/><rect x="56" width="18" height="5" rx="2.5" fill="#cfd3c8"/></svg>
</section>

<section class="faqs">
  <h2 class="h2">FAQs</h2>
  <p class="intro">Find answers to common questions about our health and wellness programs, services, and how we can support your journey to better health.</p>
  <div class="faq open" style="top:159px"><span>What types of programs do you offer?</span><span>–</span></div>
  <p class="answer">We offer a variety of programs including physiotherapy classes, wellness programs, and tailored fitness plans designed for all ages and abilities.</p>
  <div class="faq" style="top:324px"><span>How can I get started?</span><span>+</span></div>
  <div class="faq" style="top:383px"><span>Are your classes suitable for beginners?</span><span>+</span></div>
  <span class="btn" style="left:112px;top:457px;width:158px;height:42px">View Programs</span>
  <div class="photo" role="img" aria-label="Photo of a class doing medicine ball exercises in the gym" style="left:591px;top:0;width:497px;height:499px;border-radius:6px;background:linear-gradient(180deg,#8b8e88,#545650 40%,#2a2c2a 70%,#3a3c3a)"></div>
</section>

<section class="stories">
  <h2 class="h2">Client Success Stories</h2>
  <p class="sub">Hear from our clients about their transformative journeys with us.</p>
  <span class="arrow" style="left:50px;top:255px"><svg width="14" height="14" viewBox="0 0 24 24" fill="none" stroke="#fff" stroke-width="3"><path d="M15 5l-7 7 7 7"/></svg></span>
  <div class="story" style="left:112px">
    <div class="avatar" role="img" aria-label="Client portrait"></div>
    <h3>Hannah Lowe</h3><p>The Wellness Barn has completely changed my approach to fitness. Their programs are tailored and effective!</p>
    <div class="role">Fitness Enthusiast</div><div class="stars">★★★★★</div>
  </div>
  <div class="story" style="left:446px">
    <div class="avatar" role="img" aria-label="Client portrait"></div>
    <h3>Peter Grant</h3><p>I never thought I could regain my mobility. The physiotherapy classes here are a game changer!</p>
    <div class="role">Retired Veteran</div><div class="stars">★★★★★</div>
  </div>
  <div class="story" style="left:780px">
    <div class="avatar" role="img" aria-label="Client portrait"></div>
    <h3>Olivia Banks</h3><p>I love how the wellness programs fit into my hectic schedule. I feel healthier and more energetic!</p>
    <div class="role">Busy Mom</div><div class="stars">★★★★★</div>
  </div>
  <span class="arrow" style="left:1110px;top:255px"><svg width="14" height="14" viewBox="0 0 24 24" fill="none" stroke="#fff" stroke-width="3"><path d="M9 5l7 7-7 7"/></svg></span>
</section>

<footer class="site-footer">
  <h4 style="left:112px;top:68px">Stay Updated</h4>
  <p class="small" style="left:112px;top:112px;width:340px">Subscribe to our newsletter for the latest health tips and program updates.</p>
  <div class="email-field"><span>Email Address</span><svg width="14" height="14" viewBox="0 0 24 24" fill="none" stroke="#8aa24a" stroke-width="2"><rect x="3" y="5" width="18" height="14" rx="2"/><path d="M3 7l9 6 9-6"/></svg></div>
  <span class="btn" style="left:949px;top:80px;width:139px;height:44px">Subscribe</span>

  <div class="fcol" style="left:112px">
    <h4>About Us</h4>
    <p style="font-size:14px;line-height:26px;width:230px">Our core values include integrity, Collaboration, Inclusivity, and a strong Commitment to health.</p>
  </div>
  <div class="social"><i aria-label="Social link"></i><i aria-label="Social link"></i></div>
  <div class="fcol" style="left:424px">
    <h4>Main Links</h4>
    <ul><li>About Us</li><li>Programs</li><li>Testimonials</li><li>Contact Us</li></ul>
  </div>
  <div class="fcol" style="left:636px">
    <h4>Contact Us</h4>
    <ul>
      <li style="height:78px;display:flex;gap:22px"><svg width="16" height="18" viewBox="0 0 24 24" fill="none" stroke="#fff" stroke-width="2"><path d="M12 22s7-7 7-12a7 7 0 0 0-14 0c0 5 7 12 7 12z"/><circle cx="12" cy="10" r="2.5"/></svg><span style="line-height:25px;margin-top:-4px">78 Timber Lane, Riverbend,<br>Australia, 4710.</span></li>
      <li style="height:50px;display:flex;gap:22px"><svg width="16" height="16" viewBox="0 0 24 24" fill="none" stroke="#fff" stroke-width="2"><path d="M5 3h4l2 5-2.5 1.5a11 11 0 0 0 6 6L16 13l5 2v4a2 2 0 0 1-2 2A17 17 0 0 1 3 5a2 2 0 0 1 2-2"/></svg>+61 400 555 218</li>
      <li style="display:flex;gap:22px"><svg width="16" height="16" viewBox="0 0 24 24" fill="none" stroke="#fff" stroke-width="2"><rect x="3" y="5" width="18" height="14" rx="2"/><path d="M3 7l9 6 9-6"/></svg>hello@wellnessbarnhq.com</li>
    </ul>
  </div>
  <div class="fcol" style="left:954px">
    <h4>Main Links</h4>
    <ul><li>Support</li><li>Resources</li><li>Terms and Conditions</li><li>Privacy Policy</li></ul>
  </div>
  <div class="copyright">© 2025 The Wellness Barn Riverbend. All rights reserved.</div>
</footer>

</body>
</html>
```